Modern Informational OBGYN website

Looking for a modern Wordpress website for a general OBGYN practice in Florida with a specialty in High Risk Obstetrics. We had an old Joomla website that crashed and we lost most of the files. It was over 10 years old and needed a refresh anyway.

Our practice serves a multicultural patient population (white, black, Spanish and Indian) and we would like our website to reflect that diversity. Our company colors are sunshine yellow (#ECBF6D) often combined with black, white and steel blue (#7191BE) in the "life" part of our logo (attached) depending on the background. Our tagline is "We're specialist in You!" Overall the site should have a clean modern yet comfortable feel. One that portrays friendliness and competence. At least 6 pages (Home, Obstetrics, Gynecology, News, Patient Education and Resources). Rotating stock pictures or videos are fine for the headers of the pages if the design you're considering calls for it. Interesting and creative use of typography and icons are encouraged.

The home page should have a call to action to schedule an appointment as well as a link to our patient portal. Other than the home and news pages, the other pages should have a similar look and feel. The home page should have sections on "About Us", "Medical Staff" (with pictures and brief bio for 2 male doctors, 2 female midwives and 1 female nurse practitioner), "Services" and "Location". The news page will be a closed blog that will not allow comments or responses. Both the obstetrics and the gynecology pages will have an educational blurb on the respective topics followed by a list of our services for each topic. Would be nice on the obstetrics page to have information and graphics changes that occur during each trimester (but not necessary). The resource page will have sections on at least "Office Forms", Office Policies", "OB Guide" each with multiple downloadable PDF's. Also a section on "Insurance" with a list of all the major insurance plans that we take with links to their company websites. The address, link and map to our hospital and their website can also go on this page. The Patient Education Page can be broken into 3 sections Obstetrics, Gynecology which both will have definition of medical disorders followed by FAQ's and "Helpful Links" which would have links to other website for medical information.

That's all that I can think of right now. The above is to help guide you but I am flexible, if the website design dictates a better flow of information. Looking forward to seeing what you can come up with. Down the road, I will be looking to the winning designer to produce matching brochures, full, half and quarter page media ads to have on hand for the practices further needs.

Target Market(s)

Women looking medical services

Industry/Entity Type

Medical

Coding

Coded - Design and coding required

Number of Pages Required

5+ page

Font styles to use
Sans Serif
Script

Colors

Designer to choose colors to be used in the design.

Requirements
Must have
• None. See projects description for suggestions
Nice to have
• infographics like information on stages of pregnancy on the obstetrics page

```html
<!DOCTYPE html>
<html lang="en">
<head>
<meta charset="utf-8">
<title>Dawnrise OB/GYN Services</title>
<link href="https://fonts.googleapis.com/css2?family=Poppins:wght@400;500;600;700&display=swap" rel="stylesheet">
<style>
:root{
  --yellow:#f5b82e;
  --black:#000;
  --ink:#111;
  --text:#222;
  --white:#fff;
  --footer:#1b1b1b;
  --muted:#bdbdbd;
  --map-road:#f7f7f7;
  --map-base:#e3e3e3;
}
*{box-sizing:border-box;margin:0;padding:0}
html,body{width:1200px;height:4226px;overflow:hidden}
body{position:relative;font-family:"Poppins",sans-serif;color:var(--text);background:var(--white)}
.abs{position:absolute}
.btn{position:absolute;display:flex;align-items:center;justify-content:center;background:var(--yellow);color:var(--white);border-radius:30px;font-size:15px;font-weight:500}
.ph{position:absolute}
.topbar{left:0;top:0;width:1200px;height:33px;background:var(--black);color:var(--white);font-size:13px}
.topbar span{position:absolute;top:8px;display:flex;align-items:center;gap:5px}
.nav{left:0;top:33px;width:1200px;height:90px;background:var(--white)}
.logo{position:absolute;display:flex;flex-direction:column}
.logo-name{font-weight:700;color:var(--yellow);letter-spacing:1px}
.logo-sub{font-weight:600;letter-spacing:4px}
.nav a{position:absolute;top:37px;font-size:13px;color:var(--ink);text-decoration:none}
.nav a.active{color:var(--yellow)}
.hero-photo{left:0;top:123px;width:1200px;height:620px;
  background:
   radial-gradient(ellipse 260px 200px at 560px 180px,#efd3c4 0%,rgba(239,211,196,0) 100%),
   radial-gradient(ellipse 300px 240px at 800px 430px,#f1d9cd 0%,rgba(241,217,205,0) 100%),
   radial-gradient(ellipse 140px 110px at 760px 520px,#3a8fd6 0%,rgba(58,143,214,0) 100%),
   radial-gradient(ellipse 420px 300px at 330px 300px,#2f9ca8 0%,rgba(47,156,168,0) 100%),
   linear-gradient(100deg,#7c8f93 0%,#9fb1b4 25%,#d9bfb2 55%,#e6cfc6 75%,#c5d2d8 100%)}
.hero-title{left:172px;top:250px;font-size:43px;font-weight:700;color:var(--white);line-height:52px}
.hero-text{left:172px;top:368px;width:360px;font-size:14px;line-height:24px;color:var(--white);font-weight:500}
h2{font-weight:700;color:var(--ink)}
.about-title{left:172px;top:742px;font-size:46px}
.about-text{left:172px;top:807px;width:385px;font-size:13.5px;line-height:22.5px}
.about-frame{left:635px;top:658px;width:418px;height:312px;border:2px solid var(--yellow);border-radius:30px;border-left-color:transparent;border-bottom-color:transparent}
.about-photo{left:611px;top:685px;width:418px;height:311px;border-radius:30px;
  background:
   radial-gradient(ellipse 110px 160px at 330px 190px,#1f2740 0%,rgba(31,39,64,0) 100%),
   radial-gradient(ellipse 120px 170px at 110px 200px,#f4f4f4 0%,rgba(244,244,244,0) 100%),
   linear-gradient(90deg,#d6d8db 0%,#e9eaec 50%,#cfd3d8 100%)}
.staff-title{left:197px;top:1260px;font-size:48px;line-height:54px;color:var(--white)}
.member{position:absolute;width:260px;text-align:center;color:var(--white)}
.ring{width:236px;height:236px;margin:0 auto;border:2px solid var(--yellow);border-radius:50%;padding:12px}
.ring div{width:100%;height:100%;border-radius:50%}
.member h3{font-size:16px;font-weight:600;margin-top:20px}
.member p{font-size:12.5px}
.sec-title{left:0;width:1200px;text-align:center;font-size:46px}
.sec-sub{left:0;top:2058px;width:1200px;text-align:center;font-size:12px}
.card{position:absolute;width:269px;text-align:center}
.card .ph{position:static;height:183px}
.card h3{font-size:16px;font-weight:600;margin-top:14px;color:var(--ink)}
.card p{font-size:12.5px;line-height:22px;margin-top:7px;color:#333}
.news{position:absolute;overflow:hidden}
.tag{position:absolute;background:var(--yellow);color:var(--white);font-size:12px;padding:3px 10px}
.news h4{position:absolute;font-size:16px;font-weight:500;color:var(--ink);line-height:26px}
.map{left:0;top:3247px;width:1200px;height:506px;
  background:
   radial-gradient(ellipse 90px 260px at 640px 250px,#b9b9b9 0%,rgba(185,185,185,0) 100%),
   radial-gradient(ellipse 300px 200px at 150px 380px,#d2d2d2 0%,rgba(210,210,210,0) 100%),
   radial-gradient(ellipse 260px 160px at 950px 120px,#eeeeee 0%,rgba(238,238,238,0) 100%),
   linear-gradient(135deg,#e8e8e8,#dcdcdc 50%,#e6e6e6)}
.map-label{left:0;top:3472px;width:1200px;text-align:center;padding-left:0;font-size:58px;font-weight:700;color:rgba(255,255,255,.85)}
.footer{left:0;top:3753px;width:1200px;height:473px;background:var(--footer);color:var(--white)}
.f-col{position:absolute;top:130px}
.f-col h5{font-size:17px;font-weight:600;color:var(--yellow);margin-bottom:22px}
.f-col li{list-style:none;font-size:12.5px;margin-bottom:15px;display:flex;gap:9px}
.divider{position:absolute;top:110px;width:1px;height:250px;background:#444}
.divider::before{content:"";position:absolute;left:-1px;top:40px;width:3px;height:22px;background:var(--yellow)}
.social{position:absolute;top:282px;width:32px;height:32px;border-radius:50%;background:var(--white)}
.copy{position:absolute;left:172px;top:330px;font-size:12px;color:var(--muted)}
.copy b{color:var(--yellow);font-weight:400}
</style>
</head>
<body>

<div class="abs topbar">
  <span style="left:758px"><svg width="13" height="13" viewBox="0 0 24 24"><path fill="#f5b82e" d="M6.6 10.8a15 15 0 0 0 6.6 6.6l2.2-2.2a1 1 0 0 1 1-.25 11.4 11.4 0 0 0 3.6.57 1 1 0 0 1 1 1V20a1 1 0 0 1-1 1A17 17 0 0 1 3 4a1 1 0 0 1 1-1h3.5a1 1 0 0 1 1 1c0 1.25.2 2.450.57 3.57a1 1 0 0 1-.25 1z"/></svg>01 234 567 890</span>
  <span style="left:903px"><svg width="14" height="11" viewBox="0 0 24 18"><rect width="24" height="18" rx="2" fill="#f5b82e"/><path d="M1 2l11 8 11-8" stroke="#000" stroke-width="2" fill="none"/></svg>info@dawnrise.com</span>
</div>

<nav class="abs nav">
  <div class="logo" style="left:172px;top:24px">
    <span class="logo-name" style="font-size:27px;line-height:30px">DAWNRISE</span>
    <span class="logo-sub" style="font-size:7.5px;color:var(--ink);padding-left:22px">OB/GYN SERVICES</span>
  </div>
  <a class="active" style="left:465px">Home</a>
  <a style="left:542px">Obstetrics</a>
  <a style="left:640px">Gynecology</a>
  <a style="left:753px">News</a>
  <a style="left:822px">Patient Education</a>
  <a style="left:960px">Resources</a>
</nav>

<div class="ph hero-photo" role="img" aria-label="Smiling pregnant woman receiving an ultrasound scan"></div>
<svg class="abs" style="left:0;top:520px" width="1200" height="230" viewBox="0 0 1200 230">
  <path d="M0 170 C300 80 700 30 1200 22 L1200 230 L0 230Z" fill="#f5b82e"/>
  <path d="M0 218 C300 110 700 45 1200 28 L1200 230 L0 230Z" fill="#fff"/>
</svg>
<h1 class="abs hero-title">We're Specialist<br>in You!</h1>
<p class="abs hero-text">Vestibulum rhoncus enim quam, nec aliquet arcu consequat vel. Duis feugiat vicula sagittis.</p>
<div class="btn" style="left:172px;top:437px;width:271px;height:43px">Schedule an Appointment</div>

<h2 class="abs about-title">About Us</h2>
<p class="abs about-text">Lorem ipsum dolor sit amet, consectetur adipiscing elit. Cras ut dignissim nulla. Aenean pharetra facilisis diam, eget varius erat hendrerit sed. Aliquam in dui eget nulla volutpat ultricies. Praesent non arcu sed dui</p>
<div class="btn" style="left:172px;top:919px;width:156px;height:46px">Read More</div>
<div class="abs about-frame"></div>
<div class="ph about-photo" role="img" aria-label="Doctor taking notes while talking with a patient"></div>

<svg class="abs" style="left:0;top:1050px" width="1200" height="887" viewBox="0 0 1200 887">
  <path d="M0 115 C350 40 800 12 1200 8 L1200 887 L0 887Z" fill="#f5b82e"/>
  <path d="M0 158 C350 60 800 22 1200 18 L1200 887 L0 887Z" fill="#000"/>
</svg>
<h2 class="abs staff-title">Medical<br>Staff</h2>
<div class="member" style="left:471px;top:1182px"><div class="ring"><div role="img" aria-label="Portrait of a male doctor" style="background:radial-gradient(circle at 50% 80%,#e9ecef 0%,#f3f3f3 60%,#e2e2e2 100%)"></div></div><h3>Fusce et tellus</h3><p>Doctor</p></div>
<div class="member" style="left:765px;top:1182px"><div class="ring"><div role="img" aria-label="Portrait of a male doctor" style="background:radial-gradient(circle at 50% 80%,#e4e8ee 0%,#f3f3f3 60%,#e2e2e2 100%)"></div></div><h3>Fusce et tellus</h3><p>Doctor</p></div>
<div class="member" style="left:175px;top:1529px"><div class="ring"><div role="img" aria-label="Portrait of a female midwife in blue scrubs" style="background:radial-gradient(circle at 45% 85%,#2f7fd0 0%,#5d9bd8 35%,#ececec 70%)"></div></div><h3>Fusce et tellus</h3><p>Midwives</p></div>
<div class="member" style="left:471px;top:1529px"><div class="ring"><div role="img" aria-label="Portrait of a female midwife in blue scrubs" style="background:radial-gradient(circle at 50% 85%,#7fb4df 0%,#a7cbe8 35%,#ececec 70%)"></div></div><h3>Fusce et tellus</h3><p>Midwives</p></div>
<div class="member" style="left:765px;top:1529px"><div class="ring"><div role="img" aria-label="Portrait of a female nurse practitioner" style="background:radial-gradient(circle at 50% 85%,#d8dde6 0%,#e9ebef 40%,#f1f1f1 70%)"></div></div><h3>Fusce et tellus</h3><p>Nurse</p></div>

<h2 class="abs sec-title" style="top:1995px">Our Services</h2>
<p class="abs sec-sub">Lorem ipsum dolor sit amet, consectetur adipiscing elit. Cras ut dignissim nulla</p>
<div class="card" style="left:172px;top:2108px"><div class="ph" role="img" aria-label="Doctor examining a patient in a clinic" style="background:radial-gradient(ellipse 80px 90px at 70px 80px,#f4f4f4 0%,rgba(244,244,244,0) 100%),linear-gradient(135deg,#d4e6da,#9fc2b2 60%,#3d4a5a)"></div><h3>Gynecologic Care</h3><p>Aenean pharetra facilisis diam, eget varius erat hendrerit sed. Aliquam in dui eget nulla volutpat ultricies.</p></div>
<div class="card" style="left:467px;top:2108px"><div class="ph" role="img" aria-label="Woman holding a birth control pill pack" style="background:radial-gradient(ellipse 70px 100px at 140px 120px,#a7b9dc 0%,rgba(167,185,220,0) 100%),linear-gradient(135deg,#f8d3d6,#f4c3c9)"></div><h3>Birth Control</h3><p>Aenean pharetra facilisis diam, eget varius erat hendrerit sed. Aliquam in dui eget nulla volutpat ultricies.</p></div>
<div class="card" style="left:762px;top:2108px"><div class="ph" role="img" aria-label="Ultrasound scan of a pregnant belly" style="background:radial-gradient(ellipse 120px 70px at 110px 170px,#e9d8cc 0%,rgba(233,216,204,0) 100%),linear-gradient(135deg,#eef1f4,#b7c1ca 55%,#37424f)"></div><h3>Ultrasound Service</h3><p>Aenean pharetra facilisis diam, eget varius erat hendrerit sed. Aliquam in dui eget nulla volutpat ultricies.</p></div>
<div class="btn" style="left:492px;top:2449px;width:194px;height:46px">View All Services</div>

<svg class="abs" style="left:0;top:2548px" width="1200" height="700" viewBox="0 0 1200 700">
  <path d="M0 140 C350 50 800 8 1200 4 L1200 700 L0 700Z" fill="#f5b82e"/>
  <path d="M0 180 C350 70 800 20 1200 14 L1200 700 L0 700Z" fill="#000"/>
</svg>
<h2 class="abs sec-title" style="top:2655px;color:#fff">Latest News</h2>
<div class="news" style="left:172px;top:2738px;width:465px;height:358px" role="img" aria-label="Smiling patient talking with a doctor"><div style="position:absolute;inset:0;background:radial-gradient(ellipse 120px 170px at 180px 200px,#f3c9bd 0%,rgba(243,201,189,0) 100%),radial-gradient(ellipse 70px 60px at 320px 280px,#2e73d2 0%,rgba(46,115,210,0) 100%),linear-gradient(120deg,#d7e8f2,#eaf2f7 50%,#cfe1ee)"></div><span class="tag" style="left:22px;top:250px">April 18, 2022</span><h4 style="left:18px;top:285px;width:290px">Class aptent taciti sociosqu ad litora torquent</h4></div>
<div class="news" style="left:652px;top:2738px;width:379px;height:184px" role="img" aria-label="Pregnant woman smiling"><div style="position:absolute;inset:0;background:radial-gradient(ellipse 90px 110px at 300px 90px,#d8b9a3 0%,rgba(216,185,163,0) 100%),linear-gradient(90deg,#fbfbfb,#f3eeea 70%,#e6d8cc)"></div><span class="tag" style="left:22px;top:108px">April 18, 2022</span><h4 style="left:18px;top:138px;width:320px">Class aptent taciti litora torquent</h4></div>
<div class="news" style="left:652px;top:2938px;width:182px;height:158px" role="img" aria-label="Patient consultation at a desk"><div style="position:absolute;inset:0;background:radial-gradient(ellipse 60px 70px at 130px 70px,#e9c9a5 0%,rgba(233,201,165,0) 100%),linear-gradient(135deg,#b98b68,#e3cdb8)"></div><span class="tag" style="left:18px;top:66px">April 18, 2022</span><h4 style="left:8px;top:92px;width:170px">Class aptent taciti litora torquent</h4></div>
<div class="news" style="left:847px;top:2938px;width:184px;height:158px" role="img" aria-label="Smiling young woman"><div style="position:absolute;inset:0;background:radial-gradient(ellipse 60px 80px at 80px 60px,#5a4a44 0%,rgba(90,74,68,0) 100%),linear-gradient(135deg,#f0f0f0,#d8d2cd)"></div><span class="tag" style="left:26px;top:66px">April 18, 2022</span><h4 style="left:14px;top:92px;width:165px">Class aptent taciti litora torquent</h4></div>
<div class="btn" style="left:514px;top:3122px;width:172px;height:46px">View All News</div>

<div class="ph map" role="img" aria-label="Street map showing the practice location"></div>
<div class="abs map-label" style="left:0;width:1200px;text-align:center;padding-left:0">Location</div>

<footer class="abs footer">
  <div class="f-col" style="left:172px">
    <h5>Contact Info</h5>
    <ul>
      <li style="width:230px"><svg width="11" height="14" viewBox="0 0 24 32"><path fill="#f5b82e" d="M12 0a12 12 0 0 0-12 12c0 9 12 20 12 20s12-11 12-20A12 12 0 0 0 12 0zm0 17a5 5 0 1 1 0-10 5 5 0 0 1 0 10z"/></svg><span>24 Sample Ave, Lakeview,<br>FL 33101</span></li>
      <li><svg width="13" height="10" viewBox="0 0 24 18"><rect width="24" height="18" rx="2" fill="#f5b82e"/><path d="M1 2l11 8 11-8" stroke="#1b1b1b" stroke-width="2" fill="none"/></svg>info@dawnrise.com</li>
      <li><svg width="12" height="12" viewBox="0 0 24 24"><path fill="#f5b82e" d="M6.6 10.8a15 15 0 0 0 6.6 6.6l2.2-2.2a1 1 0 0 1 1-.25 11.4 11.4 0 0 0 3.6.57 1 1 0 0 1 1 1V20a1 1 0 0 1-1 1A17 17 0 0 1 3 4a1 1 0 0 1 1-1h3.5a1 1 0 0 1 1 1c0 1.25.2 2.45.57 3.57a1 1 0 0 1-.25 1z"/></svg>01 234 567 890</li>
    </ul>
  </div>
  <div class="divider" style="left:415px"></div>
  <div class="f-col" style="left:460px">
    <h5>Useful Links</h5>
    <ul><li>Home</li><li>Obstetrics</li><li>Gynecology</li><li>News</li><li>Patient Education</li><li>Resources</li></ul>
  </div>
  <div class="divider" style="left:611px"></div>
  <div class="f-col" style="left:640px">
    <h5>Services</h5>
    <ul><li>Gynecologic Care</li><li>Birth Control</li><li>Ultrasound Service</li></ul>
  </div>
  <div class="divider" style="left:788px"></div>
  <div class="logo" style="left:842px;top:165px">
    <span class="logo-name" style="font-size:38px;line-height:42px">DAWNRISE</span>
    <span class="logo-sub" style="font-size:10px;color:var(--white);padding-left:10px">OB/GYN SERVICES</span>
  </div>
  <div class="social" style="left:844px"></div>
  <div class="social" style="left:890px"></div>
  <div class="social" style="left:936px"></div>
  <div class="social" style="left:982px"></div>
  <p class="copy">© 2022 <b>Dawnrise</b>. All right reserved</p>
</footer>

</body>
</html>
```